Business Card for Makeup Artist

I need a business card designed for my makeup and hair artistry business which is primarily events and weddings focused. The card needs to be sleek, simple, stylish and appealing to women. I would prefer a white background but open to suggestions also. I also love the marble background look. I have attached some example pics. It needs to be a double sided card with logo and/or design on one side and contact details in the centre of the card on the other side. NO LOGO ON BACK. Examples attached.

Target Market(s)

Females age 14-55

Industry/Entity Type

Business

Contact Information for Business Card

Nora Vint
Principal Makeup Artist
P: 0413 925 214
E: nora@lumirabeauty.com.au
W: www.lumirabeauty.com.au

Requirements
Should not have
• No yellow, green, red or blue in the design.

```html
<!DOCTYPE html>
<html lang="en">
<head>
<meta charset="utf-8">
<title>Lumira Makeup Artistry – Business Card</title>
<link rel="stylesheet" href="https://fonts.googleapis.com/css2?family=Montserrat:wght@300;400;600;700&display=swap">
<style>
  :root {
    --stage-light: #d9d9d9;
    --stage-dark: #8a8a8a;
    --ink: #1c1c1c;
    --ink-soft: #3a3a3a;
    --paper: #ffffff;
    --accent: #e8268a;
    --front-dark: #111111;
    --front-mid: #5b5b5b;
    --skin-light: #d9b8a6;
    --skin-mid: #b08472;
    --hair: #6b4632;
    --band: #000000;
  }
  * { box-sizing: border-box; margin: 0; padding: 0; }
  html, body { width: 1200px; height: 960px; overflow: hidden; }
  body {
    font-family: "Montserrat", sans-serif;
    background: radial-gradient(ellipse at 50% 40%, var(--stage-light) 0%, var(--stage-dark) 100%);
    position: relative;
  }
  .card {
    position: absolute;
    top: 330px;
    width: 520px;
    height: 297px;
    overflow: hidden;
    box-shadow: 0 14px 30px rgba(0,0,0,0.28);
  }
  /* ---------- Front ---------- */
  .card-front {
    left: 60px;
    background: linear-gradient(135deg, var(--front-dark) 0%, var(--front-mid) 55%, #9a9a9a 100%);
  }
  .portrait-area {
    position: absolute;
    right: 0; top: 0;
    width: 62%; height: 100%;
    background:
      radial-gradient(ellipse at 55% 20%, var(--hair) 0%, rgba(107,70,50,0) 45%),
      radial-gradient(ellipse at 50% 60%, var(--skin-light) 0%, var(--skin-mid) 55%, rgba(80,60,55,0) 85%);
  }
  .front-band {
    position: absolute; left: 0; top: 0;
    width: 520px; height: 297px;
  }
  .front-url {
    font-family: "Montserrat", sans-serif;
    font-size: 11px;
    letter-spacing: 0.4px;
    fill: var(--paper);
  }
  .front-url .url-light { font-weight: 400; }
  .front-url .url-bold { font-weight: 700; }
  .brand {
    position: absolute;
    left: 150px; top: 78px;
    text-align: left;
  }
  .brand-name {
    font-size: 64px;
    font-weight: 600;
    color: var(--ink);
    line-height: 1;
    letter-spacing: 1px;
  }
  .brand-tag {
    margin-top: 8px;
    font-size: 20px;
    font-weight: 300;
    color: var(--ink);
    letter-spacing: 2px;
  }
  /* ---------- Back ---------- */
  .card-back {
    left: 620px;
    background: var(--paper);
    display: flex;
    flex-direction: column;
    align-items: center;
    justify-content: center;
    text-align: center;
  }
  .person-name {
    font-size: 38px;
    font-weight: 300;
    color: var(--ink);
    letter-spacing: 4px;
  }
  .person-role {
    margin-top: 2px;
    font-size: 13px;
    font-weight: 700;
    color: var(--accent);
    letter-spacing: 1px;
  }
  .contact-list {
    list-style: none;
    margin-top: 22px;
  }
  .contact-item {
    display: flex;
    align-items: center;
    justify-content: center;
    gap: 10px;
    font-size: 13px;
    color: var(--ink-soft);
    margin-bottom: 9px;
  }
  .contact-icon {
    width: 22px; height: 22px;
    border-radius: 50%;
    background: var(--ink);
    display: inline-flex; align-items: center; justify-content: center;
    flex-shrink: 0;
  }
</style>
</head>
<body>

<section class="card card-front" aria-label="Card front">
  <div class="portrait-area" role="img" aria-label="Portrait photograph of a woman with teal eye makeup and pink lips"></div>
  <div class="brand">
    <div class="brand-name">Lumira</div>
    <div class="brand-tag">MAKEUP ARTISTRY</div>
  </div>
  <svg class="front-band" viewBox="0 0 520 297">
    <polygon points="0,158 292,297 215,297 0,194" fill="var(--band)"/>
    <text class="front-url" transform="translate(22,189) rotate(25.5)">
      <tspan class="url-light">WWW.</tspan><tspan class="url-bold">LUMIRABEAUTY</tspan><tspan class="url-light">.COM.AU</tspan>
    </text>
  </svg>
</section>

<section class="card card-back" aria-label="Card back">
  <h1 class="person-name">Nora Vint</h1>
  <p class="person-role">PRINCIPAL MAKEUP ARTIST</p>
  <ul class="contact-list">
    <li class="contact-item">
      <span class="contact-icon">
        <svg width="12" height="12" viewBox="0 0 24 24"><path fill="#fff" d="M6.6 10.8a15 15 0 0 0 6.6 6.6l2.2-2.2c.3-.3.7-.4 1-.2 1.1.4 2.3.6 3.6.6.6 0 1 .4 1 1V20c0 .6-.4 1-1 1A17 17 0 0 1 3 4c0-.6.4-1 1-1h3.5c.6 0 1 .4 1 1 0 1.3.2 2.5.6 3.6.1.3 0 .7-.2 1z"/></svg>
      </span>
      0413 925 214
    </li>
    <li class="contact-item">
      <span class="contact-icon">
        <svg width="12" height="12" viewBox="0 0 24 24"><rect x="2" y="5" width="20" height="14" rx="1" fill="#fff"/><path d="M2 6l10 7 10-7" fill="none" stroke="#1c1c1c" stroke-width="2"/></svg>
      </span>
      nora@lumirabeauty.com.au
    </li>
    <li class="contact-item">
      <span class="contact-icon">
        <svg width="13" height="13" viewBox="0 0 24 24" fill="none" stroke="#fff" stroke-width="1.8"><circle cx="12" cy="12" r="9"/><ellipse cx="12" cy="12" rx="4" ry="9"/><path d="M3 12h18M5 7h14M5 17h14"/></svg>
      </span>
      www.lumirabeauty.com.au
    </li>
  </ul>
</section>

</body>
</html>
```